Double-sided half page marketing handout for professional association conference

We need a collatoral piece that will go into conference attendees' registration packets. Handout will be double-sided, half-letter-sized page. Working print area is 8.1" by 5.3" for each side. Can be laid out either vertically or horizontally.

One side of the piece will be focused on my firm's contact information and broad scope of services:

Contact Information:
Velmont Partners LLC
Local Government Consultants
415-630-2918
www.velmontpartners.example
info@velmontpartners.example

Services:
Bond Rating Assessments
Economic Development Consulting
Executive Dashboards
Public Policy Analysis
Governance Training & Support
Strategic Planning & Performance Management

The other side of the piece will focus on the Bond Rating Assessments (see http://www.velmontpartners.example/Pages/Bond-Rating-Assessments.aspx and attachments for more detail). This side should contain the text:

"Considering issuing debt? Bond ratings make a difference. Did you know that on an average $20 million GO debt issuance a one rating-level difference can easily equate to over $350,000 in interest cost-savings under normal market conditions?

The ratings agencies use a combined quantitative and qualitative approach to arrive at your bond rating. Our Bond Ratings Assessment shows you precisely what the agencies are looking at, provides advice as to how to frame the conversation during ratings calls, and identifies both strategic opportunities to provide upgrade pressure and specific threats that may lead to a downgrade. Call or email us to find out more or to get an example assessment."

Go to www.velmontpartners.example and see attached files for logo and a recent winning ArtHive 1/4 page advertisement for style guidance.

Target Market(s)

Highly-educated, conservative local government executives.

Industry/Entity Type

Marketing

Font styles to use
Sans Serif

Colors
3277b5
85acd3
ffffff

Requirements
Must have
• Our logo, our contact information, basic information stated in Project Description. Feel free to modify language to make more clear or understandable.
Nice to have
• We rather not just a text piece - bringing in some graphical elements would be very nice.

```html
<!DOCTYPE html>
<html lang="en">
<head>
<meta charset="utf-8">
<title>Velmont Partners – Handout</title>
<link href="https://fonts.googleapis.com/css2?family=Cinzel:wght@600&family=Lato:wght@400;700&display=swap" rel="stylesheet">
<style>
  :root{
    --blue:#0a8cf0;
    --blue-deep:#3277b5;
    --blue-soft:#85acd3;
    --dark:#2a2a2a;
    --ink:#2b2b2b;
    --white:#ffffff;
    --backdrop:#5e5e5e;
    --grey-light:#f3f3f3;
    --grey-mid:#dcdcdc;
  }
  *{box-sizing:border-box;margin:0;padding:0}
  html,body{width:1200px;height:907px;overflow:hidden}
  body{background:var(--backdrop);font-family:'Lato',sans-serif;position:relative}
  .side{position:absolute;overflow:hidden;box-shadow:0 4px 14px rgba(0,0,0,.45)}
  .side--services{left:53px;top:56px;width:518px;height:796px;background:var(--white)}
  .side--bond{left:627px;top:56px;width:515px;height:794px;background:linear-gradient(180deg,var(--grey-light) 20%,var(--white) 55%,var(--grey-mid) 95%)}
  .shapes{position:absolute;left:0;top:0}
  .wordmark{position:absolute;font-family:'Lato',sans-serif;font-weight:700;color:#3a3a3a;text-align:center;line-height:1.05}
  .side--services .wordmark{left:40px;top:310px;width:220px;font-size:30px}
  .divider{position:absolute;left:260px;top:300px;width:2px;height:100px;background:#222}
  .tagline{position:absolute;left:275px;top:312px;font-family:'Cinzel',serif;font-size:31px;line-height:1.1;color:#222;letter-spacing:.5px}
  .tab{position:absolute;background:var(--dark);border:3px solid var(--blue);border-top:none;border-radius:0 0 14px 14px;color:var(--white);font-family:'Cinzel',serif;text-align:center;display:flex;align-items:center;justify-content:center;box-shadow:0 3px 6px rgba(0,0,0,.35)}
  .side--services .tab{left:175px;top:422px;width:169px;height:67px;border-radius:14px;border-top:3px solid var(--blue);font-size:28px}
  .side--bond .tab{left:106px;top:102px;width:302px;height:95px;border-radius:0 0 16px 16px;font-size:31px;line-height:1.15;padding-top:4px}
  .intro{position:absolute;left:35px;top:508px;width:450px;font-size:12.2px;line-height:1.28;color:var(--white);text-align:justify}
  .service-list{position:absolute;left:35px;top:594px;width:450px;list-style:none;display:grid;grid-template-columns:254px 196px;row-gap:6px;font-size:11.8px;font-weight:700;color:var(--white);line-height:1.25}
  .service-list li{position:relative;padding-left:15px}
  .service-list li::before{content:"";position:absolute;left:0;top:4px;width:7px;height:7px;border-radius:50%;background:#111}
  .contact{position:absolute;font-size:11.5px;font-weight:700;color:var(--white);line-height:1.3}
  .contact svg{position:absolute;left:-14px;top:2px}
  .contact--address{left:82px;padding-left:0}
  .contact--address .indent{padding-left:14px}
  .side--services .contact--address{top:728px}
  .side--services .contact--reach{left:330px;top:728px}
  .side--bond .contact--address{left:80px;top:726px}
  .side--bond .contact--reach{left:327px;top:726px}
  .contact--reach li{list-style:none;position:relative}
  .body-copy{position:absolute;left:33px;top:249px;width:450px;font-size:11.4px;line-height:1.25;color:var(--ink);text-align:justify}
  .body-copy p{margin-bottom:13px}
  .side--bond .wordmark{left:107px;top:548px;width:300px;font-size:40px}
</style>
</head>
<body>

<section class="side side--services">
  <svg class="shapes" width="518" height="796" viewBox="0 0 518 796">
    <defs>
      <radialGradient id="hallTone" cx="60%" cy="45%" r="70%">
        <stop offset="0" stop-color="#c7876a"/>
        <stop offset=".5" stop-color="#7a3b3e"/>
        <stop offset="1" stop-color="#2c2233"/>
      </radialGradient>
    </defs>
    <rect x="0" y="0" width="518" height="170" fill="var(--blue)"/>
    <circle cx="260" cy="60" r="245" fill="var(--blue)"/>
    <circle cx="260" cy="62" r="226" fill="var(--white)"/>
    <circle cx="262" cy="68" r="214" fill="url(#hallTone)" role="img" aria-label="Photo of a speaker at a podium addressing a conference audience"/>
    <path d="M0,480 Q259,400 518,480 V796 H0 Z" fill="var(--blue)"/>
    <path d="M0,748 Q259,672 518,748" fill="none" stroke="var(--white)" stroke-width="4"/>
    <path d="M0,752 Q259,676 518,752 V796 H0 Z" fill="var(--dark)"/>
  </svg>

  <div class="wordmark">Velmont Partners LLC</div>
  <div class="divider"></div>
  <div class="tagline">Solutions<br>Delivered</div>

  <div class="tab">Services</div>

  <p class="intro">Cities and county governments are some of the most intriguing organizations around. Unfortunately, sometimes the sheer complexity of governance, service delivery, partnerships, and managing the performance of the organization can be overwhelming, leaving time only to tend to what is urgent rather than all of what is important. We are here to help.</p>

  <ul class="service-list">
    <li>Bond Rating Assessments</li>
    <li>Public Policy Analysis</li>
    <li>Economic Development Consulting</li>
    <li>Governance Training &amp; Support</li>
    <li>Executive Dashboards</li>
    <li>Strategic Planning &amp; Performance Management</li>
  </ul>

  <address class="contact contact--address">
    <svg width="10" height="12" viewBox="0 0 10 12"><path d="M5 0a4 4 0 0 1 4 4c0 3-4 8-4 8S1 7 1 4a4 4 0 0 1 4-4z" fill="#fff"/><circle cx="5" cy="4" r="1.5" fill="#2a2a2a"/></svg>
    Velmont Partners, LLC<br><span class="indent">4820 Linden Crest Way</span><br><span class="indent">Alder Springs, Texas 75210</span>
  </address>
  <ul class="contact contact--reach">
    <li><svg width="10" height="10" viewBox="0 0 10 10"><path d="M2 0l2 2-1 2 3 3 2-1 2 2-2 2C4 10 0 6 0 2z" fill="#fff"/></svg>415-630-2918</li>
    <li><svg width="10" height="8" viewBox="0 0 10 8"><rect width="10" height="8" fill="#fff"/><path d="M0 0l5 4 5-4" stroke="#2a2a2a" fill="none"/></svg>www.velmontpartners.example</li>
    <li><svg width="10" height="10" viewBox="0 0 10 10"><circle cx="5" cy="5" r="4.5" fill="#fff"/><path d="M0.5 5h9M5 .5v9" stroke="#2a2a2a" stroke-width=".8"/></svg>info@velmontpartners.example</li>
  </ul>
</section>

<section class="side side--bond">
  <svg class="shapes" width="515" height="794" viewBox="0 0 515 794">
    <path d="M0,0 H515 V128 Q257,58 0,128 Z" fill="var(--blue)"/>
    <path d="M0,132 Q257,62 515,132" fill="none" stroke="var(--white)" stroke-width="5"/>
    <path d="M0,738 Q257,668 515,738" fill="none" stroke="var(--white)" stroke-width="5"/>
    <path d="M0,742 Q257,672 515,742 V794 H0 Z" fill="var(--blue)"/>
  </svg>

  <div class="tab">Bond Rating<br>Assessments</div>

  <div class="body-copy">
    <p>Considering issuing debt? Bond ratings make a difference. Did you know that on an average $20 million GO debt issuance a one rating-level difference can easily equate to over $350,000 in interest cost-savings under normal market conditions?</p>
    <p>The ratings agencies use a combined quantitative and qualitative approach to arrive at your bond rating. Our Bond Ratings Assessment shows you precisely what the agencies are looking at, provides advice as to how to frame the conversation during ratings calls, and identifies both strategic opportunities to provide upgrade pressure and specific threats that may lead to a downgrade.</p>
    <p>Our Bond Rating Assessment will provide you a detailed report on what the agencies are looking at, what their red flags may be, and we will provide advice on how to best communicate your community's strengths to the analysts to ensure that you get the highest rating possible given your underlying financials. Then, we help prepare you and your financial team for the ratings calls, showing you exactly what to highlight as you represent the community.</p>
    <p>Call or email us to find out more or to get an example assessment.</p>
  </div>

  <div class="wordmark">Velmont Partners LLC</div>

  <address class="contact contact--address">
    <svg width="10" height="12" viewBox="0 0 10 12"><path d="M5 0a4 4 0 0 1 4 4c0 3-4 8-4 8S1 7 1 4a4 4 0 0 1 4-4z" fill="#fff"/><circle cx="5" cy="4" r="1.5" fill="#0a8cf0"/></svg>
    Velmont Partners, LLC<br><span class="indent">4820 Linden Crest Way</span><br><span class="indent">Alder Springs, Texas 75210</span>
  </address>
  <ul class="contact contact--reach">
    <li><svg width="10" height="10" viewBox="0 0 10 10"><path d="M2 0l2 2-1 2 3 3 2-1 2 2-2 2C4 10 0 6 0 2z" fill="#fff"/></svg>415-630-2918</li>
    <li><svg width="10" height="8" viewBox="0 0 10 8"><rect width="10" height="8" fill="#fff"/><path d="M0 0l5 4 5-4" stroke="#0a8cf0" fill="none"/></svg>www.velmontpartners.example</li>
    <li><svg width="10" height="10" viewBox="0 0 10 10"><circle cx="5" cy="5" r="4.5" fill="#fff"/><path d="M0.5 5h9M5 .5v9" stroke="#0a8cf0" stroke-width=".8"/></svg>info@velmontpartners.example</li>
  </ul>
</section>

</body>
</html>
```